PDF-Dokumente für Vermietung und Verwaltung von Immobilien
Zielgruppe
WohnQuell, Vermietung und Verwaltung von Immoblien
Aufgabenstellung
Wir haben ganz viele Dokumente, die als PDF erstellt werden sollen, Einheitlich im CI Design, mit Logo etc. Manche PDFS müssen ausfüllbar sein andere sind einfach nur zum Drucken. es sind ca 10-20 Word/PDF Dokumente.

```html
<!DOCTYPE html>
<html lang="de">
<head>
<meta charset="utf-8">
<title>WohnQuell – Dokumente</title>
<link rel="stylesheet" href="https://fonts.googleapis.com/css2?family=Montserrat:ital,wght@0,400;0,600;0,700;1,400&family=EB+Garamond:wght@400;600&display=swap">
<style>
:root{
  --bg:#24283a;
  --paper:#f8f8f9;
  --ink:#2a3450;
  --line:#4a5675;
  --muted:#6b7490;
  --band:#3a4a6b;
}
*{box-sizing:border-box;margin:0;padding:0}
html,body{width:1200px;height:723px;overflow:hidden;background:var(--bg)}
body{position:relative;font-family:'Montserrat',sans-serif;color:var(--ink)}
.sheet{position:absolute;top:78px;width:403px;height:565px;background:var(--paper)}
.sheet--order{left:163px}
.sheet--survey{left:664px}
.abs{position:absolute}
.brand{position:absolute;display:flex;align-items:center;gap:4px;font-family:'Montserrat',sans-serif;font-weight:600;font-size:8px;color:var(--ink)}
.brand-dot{width:6px;height:6px;border-radius:50%;background:var(--ink)}
.dots{position:absolute;border-bottom:1px dotted var(--line);height:0}
.t7{font-size:7.2px;line-height:8.6px}
.cb{display:inline-block;width:6px;height:6px;border:.8px solid var(--ink);vertical-align:-1px;margin-right:3px;background:#fff}
.band{position:absolute;left:0;right:0;bottom:0;height:7px;background:var(--band)}
.band-cut{position:absolute;bottom:0;width:4px;height:7px;background:var(--paper);transform:skewX(-22deg)}
.footer{position:absolute;top:523px;left:12px;right:10px;display:flex;font-family:'EB Garamond',serif;font-size:5.6px;line-height:7.2px;color:var(--muted)}
.footer-col{display:flex;gap:2px}
.footer-col svg{width:5px;height:5px;margin-top:1px;flex:none;fill:var(--muted)}
/* order sheet */
.recipient{left:20px;top:106px;font-family:'EB Garamond',serif;font-weight:600;font-size:8px;line-height:9.6px}
.fax{left:298px;top:107px;font-family:'EB Garamond',serif;font-weight:600;font-size:7.8px}
.price-table{left:50px;top:188px;font-size:7.2px;border-collapse:collapse}
.price-table td,.price-table th{font-weight:400;padding:0;height:9.8px;white-space:nowrap}
.price-table .num{text-align:right}
.note{left:18px;top:232px;width:375px;font-style:italic}
.info-head{left:35px;top:281px;font-weight:700;font-size:7.4px}
.info-list{left:34px;top:293px;width:350px;list-style:none}
.info-list li{position:relative;margin-bottom:4px}
.info-list li::before{content:'·';position:absolute;left:-8px}
.liability-head{left:16px;top:384px;font-weight:700;font-size:7.4px}
.liability{left:16px;top:393px;width:376px;font-size:7.1px;line-height:8.6px}
/* survey sheet */
.title{left:20px;top:20px;font-family:'EB Garamond',serif;font-weight:400;font-size:16px;color:var(--ink)}
.field{position:absolute;border:.8px solid var(--line);background:#fff}
.label{position:absolute;left:2px;top:2px;font-size:5.3px;color:var(--muted)}
.opt{position:absolute;font-size:5.5px;white-space:nowrap}
.opt.sm{font-size:4.2px}
.desc{position:absolute;font-size:3.8px;line-height:4.6px;color:var(--ink)}
</style>
</head>
<body>

<!-- Auftragsformular -->
<section class="sheet sheet--order">
  <div class="abs t7" style="left:21px;top:28px">Absender:</div>
  <div class="dots" style="left:59px;top:36px;width:204px"></div>
  <div class="abs t7" style="left:21px;top:42px">Rechnungsadresse:</div>
  <div class="abs" style="left:21px;top:51px;font-size:3.6px">(falls von Objektanschrift abweichend)</div>
  <div class="dots" style="left:107px;top:49px;width:156px"></div>
  <div class="dots" style="left:107px;top:63px;width:156px"></div>

  <div class="brand" style="left:310px;top:62px"><span class="brand-dot"></span>WohnQuell</div>

  <div class="abs recipient">Eigenheim Service<br>Westfalen GmbH<br>Lindenhofweg 7<br>44137 Dortmund</div>
  <div class="abs fax">Fax 0231 555120 - 40</div>

  <p class="abs t7" style="left:19px;top:165px;width:370px">Ich beauftrage die Eigenheim Service Westfalen GmbH mit der Erstellung der Immobilien­bewertung mit folgenden Optionen:</p>

  <table class="abs price-table">
    <tr><th style="width:100px"></th><th class="num" style="width:73px">Preis für Mitglieder</th><th class="num" style="width:78px">Nichtmitglieder</th></tr>
    <tr><td><span class="cb"></span>Immobilienbewertung</td><td class="num">89,90 €</td><td class="num">149,90 €</td></tr>
    <tr><td><span class="cb"></span>Liegenschaftskarte</td><td class="num">16,90 €</td><td class="num">19,90 €</td></tr>
    <tr><td><span class="cb"></span>Bodenrichtwertkarte</td><td class="num">7,39 €</td><td class="num">9,39 €</td></tr>
  </table>

  <p class="abs note t7">Alle genannten Preise beinhalten bereits die gültige MwSt. in Höhe von 19 %.<br>Der reduzierte Preis für Mitglieder gilt nur unter der Voraussetzung, dass für das zu bewertende Objekt eine entsprechende Mitgliedschaft besteht.</p>

  <h2 class="abs info-head">ÜBER NACHSTEHENDES WURDE ICH INFORMIERT:</h2>
  <ul class="abs info-list t7">
    <li>Eine Vorort-Besichtigung ist bei diesem Wertermittlung-Verfahren nicht erforderlich und wird daher nicht durchgeführt.</li>
    <li>Die Bearbeitung dauert mindestens 14 Tage.</li>
    <li>Erstellen Sie Fotos von allen objektrelevanten Elementen, dazu zählt: Gesamtansicht des Hauses, Gesamtansicht des Gartens, wertsteigernde Objektmerkmale wie Solaranlagen, Wintergärten, Gartenhäuser usw.</li>
    <li>Computerausdrucke der Fotos sind völlig ausreichend. Bitte keine Datenträger beilegen!</li>
  </ul>

  <h2 class="abs liability-head">HAFTUNGSAUSSCHLUSS</h2>
  <p class="abs liability">Die Ermittlung des Marktwertes und der Immobilienbewertung dienen ausschließlich der Einschätzung des voraussichtlich für eine Immobilie zu erzielenden Marktpreises und unterscheiden sich insofern von einem formalen Gutachten. Der Marktwertreport stellt kein Gutachten im Sinne des geltenden deutschen Rechts dar und basiert auf den Angaben des Kunden, statistischen Daten, Lageindikationen und mathematisch-statistischen Verfahren. Für etwaige Abweichungen von ggf. tatsächlich erzielten Kauf und/oder Verkaufspreisen und/oder Werten wird jedwede Haftung ausgeschlossen. Bezüglich der Korrektheit und Vollständigkeit der Informationen und Daten übernehmen der Eigenheimbund Westfalen e.V. und die Eigenheim Service Westfalen GmbH keine Gewähr. Dies gilt auch für Daten und Informationen, die die technischen, mathematischen und statistischen Verfahren zur Einschätzung des Marktwertes betreffen. Insgesamt ist die Haftung auf Vorsatz und grobe Fahrlässigkeit und auf den Betrag begrenzt, der für die Erstellung des Marktwertreports erhoben wird.</p>

  <footer class="footer">
    <div class="footer-col" style="width:92px"><svg viewBox="0 0 10 10"><path d="M5 0a3.5 3.5 0 0 0-3.5 3.5C1.5 6 5 10 5 10s3.5-4 3.5-6.5A3.5 3.5 0 0 0 5 0zm0 5a1.5 1.5 0 1 1 0-3 1.5 1.5 0 0 1 0 3z"/></svg><div>WohnQuell GmbH<br>Am Weidendamm 12<br>28201 Bremen</div></div>
    <div class="footer-col" style="width:80px"><svg viewBox="0 0 10 10"><path d="M2 0l2 2.5-1 1.5a6 6 0 0 0 3 3l1.5-1L10 8l-1.5 2C4 10 0 6 0 1.5z"/></svg><div>0421 5550173<br>info@wohnquell.de<br>www.wohnquell.de</div></div>
    <div class="footer-col" style="width:128px"><svg viewBox="0 0 10 10"><path d="M5 0l5 3H0zM1 4h1.5v4H1zm3.2 0h1.6v4H4.2zM7.5 4H9v4H7.5zM0 9h10v1H0z"/></svg><div>Bankverbindung:<br>Musterbank Nord<br>IBAN: DE00 1234 5678 9012 3456 78<br>BIC.: NORDDEXX000</div></div>
    <div class="footer-col"><svg viewBox="0 0 10 10"><circle cx="5" cy="3" r="2.5"/><path d="M0 10a5 4 0 0 1 10 0z"/></svg><div>Geschäftsführer:<br>Jonas Berger &amp; Lea Winter<br>USt-ID-Nr.: DE000000000<br>HRB 00000 HB</div></div>
  </footer>
  <div class="band"></div>
  <div class="band-cut" style="left:304px"></div>
</section>

<!-- Fragebogen -->
<section class="sheet sheet--survey">
  <h1 class="abs title">Fragebogen zur Immobilienbewertung</h1>
  <div class="brand" style="left:322px;top:32px"><span class="brand-dot"></span>WohnQuell</div>

  <div class="field" style="left:21px;top:51px;width:119px;height:19px"><span class="label">Mitgliedsnummer</span></div>
  <div class="field" style="left:143px;top:51px;width:119px;height:19px"><span class="label">Vorname</span></div>
  <div class="field" style="left:266px;top:51px;width:119px;height:19px"><span class="label">Nachname</span></div>
  <div class="field" style="left:21px;top:72px;width:117px;height:19px"><span class="label">Telefon</span></div>
  <div class="field" style="left:143px;top:72px;width:242px;height:19px"><span class="label">E-Mail-Adresse</span></div>
  <div class="field" style="left:21px;top:94px;width:365px;height:19px"><span class="label">Objektadresse</span></div>

  <span class="opt sm" style="left:21px;top:118px"><span class="cb"></span></span><span class="opt sm" style="left:31px;top:117px;line-height:4.6px">freistehendes<br>Einfamilienhaus</span>
  <span class="opt sm" style="left:81px;top:119px"><span class="cb"></span>2-Familienhaus</span>
  <span class="opt sm" style="left:142px;top:119px"><span class="cb"></span>Doppelhaushälfte</span>
  <span class="opt sm" style="left:201px;top:119px"><span class="cb"></span>Reihenmittelhaus</span>
  <span class="opt sm" style="left:260px;top:119px"><span class="cb"></span>Reihenendhaus</span>

  <span class="opt sm" style="left:21px;top:134px"><span class="cb"></span>Eigentumswohnung</span>
  <span class="opt sm" style="left:89px;top:135px">Mehrfamilienhaus</span>
  <div class="field" style="left:143px;top:132px;width:108px;height:19px"><span class="label">Anzahl Wohneinheiten</span></div>
  <div class="field" style="left:255px;top:132px;width:130px;height:19px"><span class="label">Miteigentum</span><span class="label" style="top:11px">Anteil &nbsp;&nbsp;&nbsp;&nbsp;&nbsp;/ &nbsp;&nbsp;&nbsp;&nbsp;&nbsp;&nbsp;&nbsp;&nbsp;&nbsp;&nbsp;&nbsp;von</span></div>

  <div class="field" style="left:21px;top:156px;width:113px;height:19px"><span class="label">Baujahr</span></div>
  <div class="field" style="left:143px;top:156px;width:119px;height:19px"><span class="label">Wohnfläche</span></div>
  <div class="field" style="left:266px;top:156px;width:120px;height:19px"><span class="label">Grundstücksfläche</span></div>

  <div class="field" style="left:21px;top:177px;width:366px;height:42px">
    <span class="label">Modernisierung – Unbedingt das Jahr angeben!</span>
    <span class="opt" style="left:2px;top:11px"><span class="cb"></span>Kernsanierung im Jahr:</span>
    <span class="opt" style="left:121px;top:12px;font-size:3.9px"><b>oder</b> (Falls eine Teilmodernisierung durchgeführt wurde, kreuzen Sie bitte Zutreffendes an.)</span>
    <span class="opt" style="left:2px;top:24px"><span class="cb"></span>Dach im Jahr:</span>
    <span class="opt" style="left:121px;top:24px"><span class="cb"></span>Leitungen im Jahr:</span>
    <span class="opt" style="left:240px;top:24px"><span class="cb"></span>Dämmung im Jahr:</span>
    <span class="opt" style="left:2px;top:33px"><span class="cb"></span>Fenster im Jahr:</span>
    <span class="opt" style="left:121px;top:33px"><span class="cb"></span>Heizung im Jahr:</span>
    <span class="opt" style="left:240px;top:33px"><span class="cb"></span>Innen im Jahr:</span>
  </div>

  <div class="field" style="left:21px;top:222px;width:367px;height:60px">
    <span class="label">Ausstattung</span>
    <span class="opt" style="left:2px;top:11px"><span class="cb"></span>einfach</span>
    <span class="opt" style="left:121px;top:11px"><span class="cb"></span>mittel</span>
    <span class="opt" style="left:240px;top:11px"><span class="cb"></span>gehoben</span>
    <p class="desc" style="left:2px;top:20px;width:108px">Mauerwerk mit Putz und Anstrich, Holzfenster mit Einfachverglasung, einfach Betondachpfannen und keine Wärmedämmung, einfaches Bad mit WC, eine elektrische Speicherheizung sowie ein Boiler für Warmwasser</p>
    <p class="desc" style="left:121px;top:20px;width:108px">Wärmedämmputz, mittlerer Wärmedämmstandard, Kunststofffenster, Rollladen und Isolierverglasung, Betondachpfannen sowie eine mittlere Wärmedämmung, 1 Bad mit Dusche und Badewanne sowie ein Gäste-WC, eine Zentralheizung</p>
    <p class="desc" style="left:240px;top:20px;width:122px">Verblendmauerwerk, Aluminiumfenster, elektr. Rollladen, Wärmeschutz- und/oder Schallschutzverglasung, hoher Wärmedämmstandard, Tondachpfannen oder Schiefer­deckung, Dachausbauten, 1-2 großzügige Bäder sowie ein Gäste-WC, Zentralheizung mit Flachheizkörpern oder Fußbodenheizung, Klimaanlagen, Solaranlagen</p>
  </div>

  <div class="field" style="left:21px;top:286px;width:368px;height:19px">
    <span class="label">Dachausbau</span>
    <span class="opt" style="left:2px;top:10px"><span class="cb"></span>nicht bekannt</span>
    <span class="opt" style="left:61px;top:10px"><span class="cb"></span>nicht ausgebaut</span>
    <span class="opt" style="left:121px;top:10px"><span class="cb"></span>nicht bekannt</span>
    <span class="opt" style="left:180px;top:10px"><span class="cb"></span>Dachgeschoss</span><span class="opt" style="left:189px;top:3px">ausgebautes</span>
    <span class="opt" style="left:240px;top:10px"><span class="cb"></span>Spitzboden</span><span class="opt" style="left:249px;top:3px">ausgebauter</span>
    <span class="opt" style="left:299px;top:10px"><span class="cb"></span>Dach u. Spitzboden</span><span class="opt" style="left:308px;top:3px">ausgebautes</span>
  </div>

  <div class="field" style="left:21px;top:309px;width:181px;height:19px">
    <span class="label">Anzahl Geschosse:</span>
    <span class="opt" style="left:99px;top:3px;font-size:3.8px;line-height:4.8px">Das (ausgebaute) Dachgeschoß wird<br>nicht als volles Geschoß gerechnet.</span>
  </div>
  <div class="field" style="left:207px;top:309px;width:182px;height:19px">
    <span class="label">Unterkellert</span>
    <span class="opt" style="left:54px;top:10px"><span class="cb"></span>zum Teil</span>
    <span class="opt" style="left:114px;top:10px"><span class="cb"></span>voll</span>
  </div>

  <div class="field" style="left:21px;top:332px;width:181px;height:19px">
    <span class="label">Gesamtzustand des Hauses</span>
    <span class="opt" style="left:2px;top:10px"><span class="cb"></span>gut</span>
    <span class="opt" style="left:61px;top:10px"><span class="cb"></span>mittel</span>
    <span class="opt" style="left:121px;top:10px"><span class="cb"></span>mäßig</span>
  </div>
  <div class="field" style="left:207px;top:332px;width:182px;height:19px">
    <span class="label">Anzahl Garagen:</span><span class="label" style="left:99px">Anzahl Stellplätze:</span>
  </div>

  <div class="field" style="left:21px;top:355px;width:313px;height:19px">
    <span class="label">Erbbaurecht</span>
    <span class="opt" style="left:2px;top:10px"><span class="cb"></span>nein</span>
    <span class="opt" style="left:61px;top:10px"><span class="cb"></span>ja</span>
    <span class="opt" style="left:121px;top:10px"><span class="cb"></span>Bes. Vorbehalte &nbsp; Beginn (Jahr):</span>
    <span class="opt" style="left:240px;top:10px">Vertragsablaufjahr:</span>
  </div>
  <div class="field" style="left:338px;top:355px;width:51px;height:19px">
    <span class="label">Erbbauzins p.a.</span><span class="opt" style="left:2px;top:10px">…………… €</span>
  </div>

  <div class="field" style="left:21px;top:378px;width:369px;height:19px">
    <span class="label">Besonderheiten im Grundbuch</span>
    <span class="opt" style="left:2px;top:10px"><span class="cb"></span>Wohnrechte</span>
    <span class="opt" style="left:61px;top:10px"><span class="cb"></span>Nießbrauchrechte</span>
    <span class="opt" style="left:180px;top:10px"><span class="cb"></span>Wege u. Leitungsrechte</span>
    <span class="opt" style="left:299px;top:10px"><span class="cb"></span>keine</span>
  </div>

  <div class="field" style="left:21px;top:401px;width:369px;height:19px">
    <span class="label">Mieteinnahmen:</span>
    <span class="opt" style="left:2px;top:10px"><span class="cb"></span>nein</span>
    <span class="opt" style="left:61px;top:10px"><span class="cb"></span>ja, wie hoch (Kaltmiete pro Monat)? &nbsp;&nbsp;&nbsp;……………………</span>
  </div>

  <div class="field" style="left:21px;top:424px;width:370px;height:66px">
    <span class="label">Notizen/Hinweise</span>
    <span class="label" style="top:58px">Anzahl Objektfotos:</span>
    <span class="label" style="left:103px;top:58px">(Objektfotos bitte mit Mitglieds-Nr. versehen.)</span>
  </div>

  <div class="field" style="left:209px;top:495px;width:183px;height:19px">
    <span class="label" style="top:11px">Unterschrift</span>
  </div>

  <footer class="footer" style="top:522px;left:19px">
    <div class="footer-col" style="width:92px"><svg viewBox="0 0 10 10"><path d="M5 0a3.5 3.5 0 0 0-3.5 3.5C1.5 6 5 10 5 10s3.5-4 3.5-6.5A3.5 3.5 0 0 0 5 0zm0 5a1.5 1.5 0 1 1 0-3 1.5 1.5 0 0 1 0 3z"/></svg><div>WohnQuell GmbH<br>Am Weidendamm 12<br>28201 Bremen</div></div>
    <div class="footer-col" style="width:80px"><svg viewBox="0 0 10 10"><path d="M2 0l2 2.5-1 1.5a6 6 0 0 0 3 3l1.5-1L10 8l-1.5 2C4 10 0 6 0 1.5z"/></svg><div>0421 5550173<br>info@wohnquell.de<br>www.wohnquell.de</div></div>
    <div class="footer-col" style="width:128px"><svg viewBox="0 0 10 10"><path d="M5 0l5 3H0zM1 4h1.5v4H1zm3.2 0h1.6v4H4.2zM7.5 4H9v4H7.5zM0 9h10v1H0z"/></svg><div>Bankverbindung:<br>Musterbank Nord<br>IBAN: DE00 1234 5678 9012 3456 78<br>BIC.: NORDDEXX000</div></div>
    <div class="footer-col"><svg viewBox="0 0 10 10"><circle cx="5" cy="3" r="2.5"/><path d="M0 10a5 4 0 0 1 10 0z"/></svg><div>Geschäftsführer:<br>Jonas Berger &amp; Lea Winter<br>USt-ID-Nr.: DE000000000<br>HRB 00000 HB</div></div>
  </footer>
  <div class="band"></div>
  <div class="band-cut" style="left:314px"></div>
</section>

</body>
</html>
```